I teach courses in Quick Phrases for Rescue Crews, paramedics, firefighters, nurses and all other Emergency related occupations. I need to let them know that this course is available and post this card on the bulletin boards of fire stations and other related offices. It has to call their attention.

Industry/Entity Type

Call

Colors
ec2027

Requirements
Must have
• I would like a picture of a paramedic and a nurse. It can also have a firefighter as a second choice. Red is a good color to call attention. I am including a picture of me and a short bio to go on the reverse but this is not a must. I do not want my picture in the front.
I am thinking of an over sized postcard
Nice to have
• The title can be "Quick Phrases for Rescue Crews" in full or "Quick Phrases for RC's " depending on the fact that the whole name may be too long to make it stand out enough
Should not have
• I do not know if my picture has come out in the right frame I see the cut is not right in the uploead. You might need to frame it right.

```html
<!DOCTYPE html>
<html lang="en">
<head>
<meta charset="utf-8">
<title>Quick Phrases for Rescue Crews – Postcard</title>
<link href="https://fonts.googleapis.com/css2?family=Roboto+Condensed:ital,wght@0,300;0,400;0,700;1,700&display=swap" rel="stylesheet">
<style>
  :root{
    --stage:#0f2a38;
    --card-dark:#1e2023;
    --ink:#111418;
    --white:#ffffff;
    --accent:#f5c312;
    --sky:#6fb6e6;
    --sky-deep:#3d8ccc;
    --leaf:#b7dc7c;
    --stamp:#e6eef7;
  }
  *{margin:0;padding:0;box-sizing:border-box}
  html,body{width:1200px;height:1000px;overflow:hidden;background:var(--stage)}
  body{position:relative;font-family:"Roboto Condensed",sans-serif}

  .card{position:absolute;width:652px;height:505px;box-shadow:0 12px 30px rgba(0,0,0,.45)}

  /* Reverse side */
  .card--back{left:95px;top:105px;color:var(--ink);
    background:
      radial-gradient(ellipse 70% 60% at 0% 100%, rgba(183,220,124,.9), transparent 60%),
      linear-gradient(100deg, var(--sky-deep) 0%, var(--sky) 30%, #cfe6f6 55%, #fbfdfd 75%, #f3f8ec 100%);}
  .portrait{position:absolute;left:38px;top:35px;width:118px;height:160px;border:2px solid var(--white);
    background:linear-gradient(160deg,#8a5a3c,#c88a68 55%,#e8c2a4)}
  .bio-name{position:absolute;left:185px;top:36px;font-size:31px;font-weight:700;letter-spacing:-.3px}
  .bio-cred{position:absolute;left:185px;top:75px;font-size:17px;font-weight:700}
  .bio-intro{position:absolute;left:185px;top:99px;width:290px;font-size:14px;line-height:21px}
  .bio-body{position:absolute;left:38px;top:208px;width:280px;font-size:14px;line-height:21px}
  .bio-contact{position:absolute;left:38px;top:323px;font-size:19.5px;font-weight:700;line-height:29px}
  .stamp{position:absolute;left:505px;top:30px;width:115px;height:115px;background:var(--stamp);opacity:.85}

  /* Front side */
  .card--front{left:480px;top:392px;background:var(--card-dark);color:var(--white);overflow:hidden}
  .hero-photo{position:absolute;right:0;top:0;width:420px;height:100%;
    background:linear-gradient(90deg,var(--card-dark) 0%,rgba(60,64,70,.6) 35%,#4a4d52 60%,#2a2c30 100%)}
  .title{position:absolute;left:37px;top:32px;font-size:37px;font-weight:300;letter-spacing:-.5px;white-space:nowrap}
  .title em{color:var(--accent);font-weight:700;font-style:italic}
  .lead{position:absolute;left:37px;top:86px;width:400px;font-size:16.5px;font-weight:700;line-height:21px}
  .benefits{position:absolute;left:37px;top:152px;list-style:none;font-size:13.5px;line-height:21px;font-weight:300}
  .benefits li::before{content:"•";display:inline-block;width:16px;font-size:10px;vertical-align:1px}
  .details{position:absolute;left:37px;top:336px;font-size:16px;font-weight:700;line-height:24px}
  .call-line{position:absolute;left:37px;top:414px;font-size:15.5px;font-weight:700;white-space:nowrap}
  .call-line strong{color:var(--accent);font-size:27px;vertical-align:-3px}
  .badge{position:absolute;width:98px;height:98px;border-radius:50%;border:3px solid var(--white)}
  .badge--fire-a{left:484px;top:227px;background:radial-gradient(circle at 65% 40%,#ffb43a,#d04a12 50%,#2a1a12)}
  .badge--responder{left:495px;top:333px;background:linear-gradient(160deg,#6e8a5a,#3b4a38 60%,#1c2026)}
  .badge--fire-b{left:391px;top:378px;background:radial-gradient(circle at 50% 35%,#ff9a2e,#b8370f 55%,#2a120c)}
</style>
</head>
<body>

<section class="card card--back" aria-label="Postcard reverse with instructor bio">
  <div class="portrait" role="img" aria-label="Portrait photo of the instructor"></div>
  <h2 class="bio-name">Marisol Dunmore</h2>
  <p class="bio-cred">B.A., C.P.C.C.,</p>
  <p class="bio-intro">brings to the classroom a superb blend of skills, knowledge and experience that allows her to design and teach unique courses in Spanish as a second language.</p>
  <p class="bio-body">Her native Spanish, "castellano "from Argentina, her many years of experience in linguistics and her studies in Life Coaching, Transformational Coaching and various other fields assures you a one of a kind language learning experience.</p>
  <p class="bio-contact">Find more on Friendsite&nbsp; as<br>Marisol Dunmore or<br>Call (310) 555 0142</p>
  <div class="stamp" aria-hidden="true"></div>
</section>

<section class="card card--front" aria-label="Postcard front">
  <div class="hero-photo" role="img" aria-label="Photo of a smiling paramedic in uniform with a patient on a stretcher behind her"></div>
  <h1 class="title">Quick Phrases for <em>Rescue Crews</em></h1>
  <p class="lead">Course designed specifically for paramedics, firefighters, nurses and all other emergency related occupations.</p>
  <ul class="benefits">
    <li>Learn exactly the language you need for each emergency situation</li>
    <li>Bring down the language barrier with your Spanish-speaking patients</li>
    <li>Earn credits for your job or resume</li>
    <li>Meet new people while you practice</li>
    <li>Build a solid base for speaking Spanish in any situation sounding like a native</li>
    <li>Learn easily with " whole brain learning tools"</li>
    <li>Learn more about yourself and how you learn best</li>
    <li>Have great fun and de-stress</li>
  </ul>
  <p class="details">Small groups and one-on-one coaching/tutoring sessions<br>available in Bayview, California.<br>For more information find us on Friendsite as</p>
  <p class="call-line">Marisol Dunmore or <strong>Call: 310 555 0142</strong></p>
  <div class="badge badge--fire-a" role="img" aria-label="Photo of a firefighter spraying water at flames"></div>
  <div class="badge badge--responder" role="img" aria-label="Photo of a male paramedic outdoors"></div>
  <div class="badge badge--fire-b" role="img" aria-label="Photo of two firefighters in front of a blaze"></div>
</section>

</body>
</html>
```